Diesel injection diagnostics and repairs

I am after a business card design for my business.
The business; repairs diesel fuel systems on 4wds, trucks, earthmoving equipment,can do mobile repairs and diagnostics
The business design can basic but effective, I guess some colours such as green and black or even blue......
The end result should reflect the business name and logo and what the business can do

Industry/Entity Type

Business

Contact Information for Business Card

TB Diesel Injection PTY LTD
tb_diesel@mailbox-example.net
Nathan Bowers
0491570156

```html
<!DOCTYPE html>
<html lang="en">
<head>
<meta charset="utf-8">
<title>TB Diesel Injection – Business Card</title>
<link rel="stylesheet" href="https://fonts.googleapis.com/css2?family=Mulish:ital,wght@0,400;0,700;0,800;1,300;1,400;1,700&display=swap">
<style>
  :root {
    --page: #e6e7e8;
    --card: #ffffff;
    --card-edge: #8a8a8a;
    --band: #000000;
    --accent: #1ea6e0;
    --ink: #1a1a1a;
    --light: #ffffff;
  }
  * { margin: 0; padding: 0; box-sizing: border-box; }
  html, body {
    width: 929px; height: 1200px; overflow: hidden;
    background: var(--page);
  }
  body { position: relative; font-family: "Mulish", sans-serif; }
  .card {
    position: absolute; left: 118px; width: 711px; height: 435px;
    background: var(--card); border: 1px solid var(--card-edge);
  }
  .card--front { top: 69px; }
  .card--back { top: 583px; }
  .card svg { display: block; width: 100%; height: 100%; }
  .band { fill: var(--band); }
  .brand-name { fill: var(--accent); font-family: "Mulish", sans-serif; font-weight: 800; }
  .tagline { fill: var(--ink); font-family: "Mulish", sans-serif; font-style: italic; font-weight: 300; font-size: 28px; }
  .holder-name { fill: var(--accent); font-family: "Mulish", sans-serif; font-weight: 700; font-size: 38px; }
  .contact { fill: var(--light); font-family: "Mulish", sans-serif; font-size: 27px; }
  .contact-label { font-weight: 700; font-style: italic; }
</style>
</head>
<body>

<section class="card card--front" aria-label="Card front">
  <svg viewBox="0 0 711 435" xmlns="http://www.w3.org/2000/svg">
    <polygon class="band" points="0,239 380,84 622,84 622,333 0,333"/>
    <text class="brand-name" text-anchor="end">
      <tspan x="604" y="190" font-size="96">TB</tspan>
      <tspan x="604" y="260" font-size="44">Diesel</tspan>
      <tspan x="604" y="310" font-size="44">Injection</tspan>
    </text>
    <text class="tagline" x="72" y="366">Diagnostics &amp; Repairs</text>
  </svg>
</section>

<section class="card card--back" aria-label="Card back">
  <svg viewBox="0 0 711 435" xmlns="http://www.w3.org/2000/svg">
    <polygon class="band" points="0,232 380,84 622,84 622,333 0,333"/>
    <text class="holder-name" x="107" y="167" transform="rotate(-21 107 167)">Nathan Bowers</text>
    <text class="contact" x="78" y="256" transform="rotate(-12 78 256)"><tspan class="contact-label">T:</tspan> 0491570156</text>
    <text class="contact" x="78" y="300" transform="rotate(-5.6 78 300)"><tspan class="contact-label">E:</tspan> tb_diesel@mailbox-example.net</text>
  </svg>
</section>

</body>
</html>
```